依頼詳細
弊社のトップページのリニューアルをお願いします。

内容はMRキャップ(弊社メーカーにて販売)とカチモア(ネジ通販サイト)の2点に絞りこみ出来るだけシンプルなデザインにしてほしい。
その他のページの改良は未定ですが、満足いくものが出来れば全面リニューアルの際に
再度ご依頼させて頂きます。
サイトURL
http://www.hanamizucorp.co.jp/
ページ数
1ページ
希望イメージ
シンプル 複雑
単色 カラフル
暗い 明るい
日常 高級
遊び心 厳粛
未来的 伝統的
女性的 男性的
希望する色
青系、水色系、グレー系
納品ファイル
• 高解像度JPG (.jpg)
• イラストレーター形式 (.ai)
• フォトショップ形式 (.psd)
• PNG形式 (.png)
補足説明
画像素材も付けておきます。
宜しくお願いします。
■ 選んだ理由

素晴らしいセンスと柔軟な対応で、気持ちよく進めることが出来ました。
スキルも幅広い方なので、今後ご依頼をさせて頂く際心強いと思い決めさせていただきました。

■ 提案者全員のお礼・コメント

当選決定が遅くなってしまい申し訳ありませんでした。
クオリティの高い画像をありがとうございました。
また機会がありましたら、よろしくお願いいたします。

```html
<!DOCTYPE html>
<html lang="ja">
<head>
<meta charset="utf-8">
<title>株式会社ハナミズ</title>
<link href="https://fonts.googleapis.com/css2?family=Noto+Sans+JP:wght@400;500;700;900&display=swap" rel="stylesheet">
<style>
:root{
  --blue:#3a7fe0;
  --blue-dark:#2a62b8;
  --navy:#0a1a3a;
  --gray-bg:#eeeeee;
  --line:#d4d4d4;
  --text:#444;
  --heading:#333;
  --muted:#777;
  --orange:#e8891f;
  --white:#fff;
}
*{margin:0;padding:0;box-sizing:border-box}
html,body{width:707px;height:1200px;overflow:hidden}
body{font-family:"Noto Sans JP",sans-serif;color:var(--text);background:var(--white);position:relative}
.site-header{height:28px;display:flex;justify-content:space-between;align-items:stretch;background:var(--white)}
.brand{display:flex;align-items:center;gap:5px;padding-left:10px}
.brand-mark{width:10px;height:10px;background:var(--blue)}
.brand-name{font-size:10px;font-weight:700;color:var(--blue-dark);line-height:1}
.global-nav{display:flex;background:var(--blue);width:470px}
.global-nav a{flex:1;color:var(--white);text-decoration:none;font-size:9px;display:flex;align-items:center;justify-content:center;border-left:1px solid rgba(255,255,255,.25)}
.hero{position:relative;height:255px;overflow:hidden;color:var(--white);text-align:center}
.hero-visual{position:absolute;inset:0;background:radial-gradient(ellipse 60% 55% at 50% 105%,#7fb8ff 0%,#2a5fb0 25%,#0f2a5a 55%,var(--navy) 100%)}
.hero-title{position:relative;margin-top:66px;font-size:29px;font-weight:900;letter-spacing:1px}
.hero-sub{position:relative;margin-top:6px;font-size:9px;letter-spacing:1.5px}
.hero-lead{position:relative;margin-top:72px;font-size:9px}
.section{position:relative}
.section-cap{height:271px;background:var(--gray-bg);border-top:4px solid var(--line)}
.cap-body{position:absolute;left:106px;top:26px;width:238px}
.cap-title{font-size:24px;font-weight:700;color:var(--heading);margin-bottom:12px}
.cap-body p{font-size:7px;line-height:1.75;color:var(--muted);margin-bottom:6px}
.cap-photo{position:absolute;left:380px;top:42px;width:220px;height:150px;background:radial-gradient(circle at 50% 50%,#c9ced6,#8e96a3 70%,#eeeeee 100%);border-radius:6px}
.more-btn{position:absolute;left:207px;width:276px;height:28px;background:linear-gradient(var(--blue),var(--blue-dark));border-radius:4px;color:var(--white);font-size:11px;font-weight:700;display:flex;align-items:center;justify-content:center;text-decoration:none}
.more-btn svg{position:absolute;right:-12px;top:0}
.section-cap .more-btn{top:222px}
.section-shop{height:246px;background:var(--white)}
.shop-brand{position:absolute;left:100px;top:64px}
.shop-tag{font-size:9px;font-weight:700;color:var(--orange)}
.shop-name{margin-top:8px;font-size:24px;font-weight:700;color:var(--heading);line-height:1.2}
.shop-text{position:absolute;left:380px;top:34px;width:230px}
.shop-text p{font-size:7px;line-height:1.75;color:var(--muted);margin-bottom:8px}
.section-shop .more-btn{top:188px}
.section-news{height:343px;background:var(--gray-bg);border-top:4px solid var(--line)}
.news-title{text-align:center;font-size:22px;font-weight:700;color:var(--heading);padding-top:62px}
.news-list{position:absolute;left:100px;top:126px;width:446px;height:176px;background:var(--white);border:1px solid var(--line);overflow:hidden;list-style:none}
.news-list li{padding:6px 18px 6px 10px;border-bottom:1px solid var(--line);font-size:8px;line-height:1.6}
.news-list time{display:block;color:var(--heading)}
.news-scroll{position:absolute;right:0;top:0;width:8px;height:100%;background:#f2f2f2;border-left:1px solid var(--line)}
.site-footer{position:absolute;left:0;top:1143px;width:707px;height:57px;background:var(--blue);color:var(--white);text-align:center}
.footer-links{padding-top:14px;font-size:8px;display:flex;justify-content:center;gap:14px}
.copyright{margin-top:12px;font-size:7px}
</style>
</head>
<body>
<header class="site-header">
  <div class="brand"><i class="brand-mark"></i><span class="brand-name">株式会社ハナミズ</span></div>
  <nav class="global-nav">
    <a href="#">製品案内</a><a href="#">カチモア購入</a><a href="#">プレスリリース</a><a href="#">企業情報</a><a href="#">お問い合わせ</a>
  </nav>
</header>

<section class="hero">
  <div class="hero-visual" role="img" aria-label="宇宙から見た青く輝く地球の風景"></div>
  <h1 class="hero-title">ネジ革命を推進する会社</h1>
  <p class="hero-sub">COMPANY THAT PROMOTES SCREW REVOLUTION</p>
  <p class="hero-lead">株式会社ハナミズは、ボルト、ナット、ネジ、ワッシャーなどの締結部品を通じて、ものづくりの未来を支えています。</p>
</section>

<section class="section section-cap">
  <div class="cap-body">
    <h2 class="cap-title">MRキャップ</h2>
    <p>MRボルト・ナットキャップは当社オリジナルの締結部品保護キャップです。錆や汚れからボルトとナットを守り、見た目も美しく仕上げます。</p>
    <p>屋内外の設備、建築、機械など幅広い用途でご使用いただけます。サイズやカラーも豊富にご用意しています。</p>
    <p>安全性と耐久性を兼ね備えた製品として、多くの現場で採用されています。</p>
  </div>
  <div class="cap-photo" role="img" aria-label="グレーと白の各種ボルト・ナットキャップの製品写真"></div>
  <a class="more-btn" href="#">詳しくはこちら
    <svg width="24" height="28" viewBox="0 0 24 28"><path d="M0 0 L24 14 L0 28 Z" fill="#2a62b8"/></svg>
  </a>
</section>

<section class="section section-shop">
  <div class="shop-brand">
    <p class="shop-tag">業務用・DIY用でネジをお探しの方は</p>
    <p class="shop-name">カチモア</p>
  </div>
  <div class="shop-text">
    <p>ネジ販売サイト「カチモア」では、ネジ、ボルト、ナット、ワッシャーなど約十万点の商品を一本から購入できます。</p>
    <p>業務用の大量注文から、DIY用の少量購入まで幅広く対応。ご注文は二十四時間受け付けております。</p>
    <p>ご不明な点はお気軽にお問い合わせください。専門スタッフが丁寧にご案内いたします。</p>
  </div>
  <a class="more-btn" href="#">詳しくはこちら
    <svg width="24" height="28" viewBox="0 0 24 28"><path d="M0 0 L24 14 L0 28 Z" fill="#2a62b8"/></svg>
  </a>
</section>

<section class="section section-news">
  <h2 class="news-title">新着情報</h2>
  <ul class="news-list">
    <li><time>2015-01-20</time>■ニュースリリースを更新しました。<br>ネジ通販サイト「カチモア」の新規掲載情報を更新しました。<br>【詳細は、こちらをクリック】</li>
    <li><time>2015-01-10</time>■ニュースリリースを更新しました。<br>新製品のご案内を掲載しました。<br>【詳細は、こちらをクリック】</li>
    <li><time>2015-03-04</time>■ニュースリリースを更新しました。<br>展示会出展のお知らせを掲載しました。</li>
  </ul>
  <div class="news-scroll" style="left:538px;top:126px;height:176px;right:auto"></div>
</section>

<footer class="site-footer">
  <div class="footer-links"><span>MRキャップ・ナットキャップ</span><span>｜</span><span>業務用・DIY用ネジ販売サイト「カチモア」</span><span>｜</span><span>会社概要</span><span>｜</span><span>プライバシーポリシー</span></div>
  <p class="copyright">Copyright (C) Hanamizu corporation All rights reserved.</p>
</footer>
</body>
</html>
```